Bertuzzo Italian Spring Water!

We need a label for a new drinking water brand called "Sorgente Bertuzzo". It is water from the ancient and pure Fountain of Bertuzzo in the Italian countryside. The water has special health qualities that some believe can make you healthier and even cure some illnesses. The look of the label should make people think: clean, healthy, pure, Italian, and could include imagery of Matteo Corsaghi or Italy or hills or something totally different - something new and cool!

Please use the Italian words "Sorgente Bertuzzo" as the main name on the label and the logo, and if you want to try to include the English wording "Fountain of Bertuzzo" in a smaller way that might be interesting.

Sick

Target Market(s)

Health conscious water consumers

Industry/Entity Type

Health food / water

Requirements
Must have
• Eye-popping graphics

```html
<!DOCTYPE html>
<html lang="en">
<head>
<meta charset="utf-8">
<title>Sorgente Bertuzzo – Label</title>
<link rel="stylesheet" href="https://fonts.googleapis.com/css2?family=Marcellus&family=Montserrat:wght@500&family=Tinos:ital@1&display=swap">
<style>
  :root {
    --backdrop: #e4e4e4;
    --label-white: #f7f8f9;
    --brand-blue: #0d4f9c;
    --ink: #222222;
    --peak-light: #dce8f3;
    --peak-mid: #8fb1d2;
    --peak-deep: #5f87b3;
  }
  * { margin: 0; padding: 0; box-sizing: border-box; }
  html, body {
    width: 1200px; height: 894px; overflow: hidden;
    background: var(--backdrop);
  }
  .canvas { position: relative; width: 1200px; height: 894px; }
  .label {
    position: absolute; left: 404px; top: 17px;
    width: 392px; height: 860px;
    background: var(--label-white);
    box-shadow: 0 6px 24px rgba(0,0,0,0.12);
    text-align: center;
  }
  .brand-name {
    position: absolute; top: 72px; left: 0; width: 100%;
    font-family: "Marcellus", serif;
    color: var(--brand-blue);
    font-size: 62px; line-height: 74px;
    font-weight: 400;
  }
  .brand-name span { display: block; }
  .water-line {
    position: absolute; top: 220px; left: 28px; right: 28px;
    display: flex; align-items: center; gap: 16px;
    font-family: "Marcellus", serif;
    color: var(--ink); font-size: 34px;
  }
  .water-line::before, .water-line::after {
    content: ""; flex: 1; height: 1.5px; background: var(--brand-blue);
  }
  .scenery {
    position: absolute; top: 290px; left: 0; width: 100%; height: 356px;
    background:
      linear-gradient(180deg, rgba(247,248,249,0) 60%, var(--label-white) 100%),
      radial-gradient(ellipse 60% 70% at 25% 55%, var(--peak-mid), transparent 70%),
      radial-gradient(ellipse 55% 75% at 78% 50%, var(--peak-deep), transparent 70%),
      linear-gradient(180deg, var(--label-white) 0%, var(--peak-light) 30%, var(--peak-mid) 55%, var(--label-white) 100%);
  }
  .product-type {
    position: absolute; top: 650px; left: 0; width: 100%;
    font-family: "Marcellus", serif;
    font-weight: 400;
    color: var(--brand-blue);
    font-size: 45px; line-height: 55px;
  }
  .product-type span { display: block; }
  .product-rule {
    position: absolute; top: 763px; left: 32px; right: 32px; height: 3px;
    background: linear-gradient(90deg, rgba(13,79,156,0.1), var(--brand-blue) 50%, rgba(13,79,156,0.1));
  }
  .source-name {
    position: absolute; top: 782px; left: 0; width: 100%;
    font-family: "Montserrat", sans-serif; font-weight: 500;
    color: var(--ink); font-size: 15px; letter-spacing: 3px;
  }
  .volume {
    position: absolute; top: 826px; left: 0; width: 100%;
    font-family: "Tinos", serif; font-style: italic;
    color: #444; font-size: 23px;
  }
</style>
</head>
<body>
<div class="canvas">
  <div class="label">
    <h1 class="brand-name"><span>SORGENTE</span><span>BERTUZZO</span></h1>
    <div class="water-line">WATER</div>
    <div class="scenery" role="img" aria-label="Photograph of snowy blue mountain peaks above soft white clouds"></div>
    <h2 class="product-type"><span>ITALIAN</span><span>SPRING WATER</span></h2>
    <div class="product-rule"></div>
    <p class="source-name">FOUNTAIN OF BERTUZZO</p>
    <p class="volume">1000ml</p>
  </div>
</div>
</body>
</html>
```